UPDATE: Please see File 2 for the most recent content, the precise content to include into the design. Also, we want an image that will clearly present the 7-Step Management Process for our Framework for High Performance.

When someone clicks on any portion of the image you would design, it would open up a box that would give all of the details and subtext of that particular category. I trust you guys as designers to figure out this challenge. I am a content expert. I know the answers as to how to run a more effective business, but I don't have any idea how to effectively present my business process graphically! To be clear, these are only ideas; I need you to figure out this challenge. I know the business principles very well, but I don't know how to express them in a well designed image that can be clicked-on and then opens up to present the content under each category.

The image must be printable as well.

We need a clear, crisp way to present our unique 7-Step business process and philosophy such that executives can quickly and clearly assess our principles and business management process. We need a very professional, crisp, catchy design to incorporate our 7 categories and the written process points under each category headline.

I have attached what we are currently using, and it is not good! We print it out on a regular piece of paper and the font is too small and hard to read. Not thrilled with the colors, either. We need a totally new concept. A totally new design and process for executives to quickly and easily access this information.

This is the culmination of 35 years of consulting work, all boiled down into a single page, and candidly, the content is fantastic! But I need a MUCH better, cleaner, more crisp, more catchy and far more professional way to present this and give it to clients.

PLEASE NOTE: We will adjust some of the text or subtract or delete a word or line here or there. What is most important is your design approach to figure out how to present this quantity of information in an easy to read, easy to understand format.

I have attached updated content for you to cut and paste into your design.

I am extremely disappointed. I committed a huge budget to this project after your site "encouraged" me to go-hard on the money, which I did, and now I am getting just terrible designs. These are not what I am looking for, many have just copied my ideas without any original thought. I have sent Pixel Bazaar multiple messages about this and nothing is changing. Plus, your people are not seemingly reading the full brief, etc. Either just cancel the entire project or help me re-write the brief to get people to better understand, or extend this another 10 days or something. I am really at my wit's end here. Please see all of my other correspondence with you about this project. The last project went super great, so I was excited about this one, but so far, I am just so disappointed with the proposed solutions to my design challenge. Mark Dervin markTdervin@quillpost.example (555) 317-4096

Target Market(s)

Business Executives. Fortune 500 Companies. Millennials. Managers. Business Executives. INDUSTRIES: High Tech, Banking, Finance, Insurance, Pharmaceuticals, Sales Management. All high-end senior level business executives

Industry/Entity Type

Business

Logo Text

Still working on this! Need Help!

Font styles to use
Sans Serif

Colors
7fa7d0
0355a3
fef6f1
f37022
ffc214
9bcb3c
3277b5
ec1f27
fbed22

Requirements
Must have
• Professional. Crisp. Clear. Punchy. Easy to read. Easy to understand. The problem we have is that we need to retain all of these points, but it is a lot to read, I know. But these are all timeless business principles that we want our clients to be able to easily see, read and access in the moment. The current format of 8 1/2 x 11 inch paper doesn't seem to be adequate. Do we make it multiple pages, do we use a digital graphic and they can click on a particular section and then that section opens-us a box of additional text? We are open to any solution, but it must be clear, crisp, easy to read and look very highly designed, highly professional.

The graphic design is most important. it must be printable and it should be set up so that if you click on any category header, the content behind that header will open up in a pop up screen to give you all the details.
Nice to have
• A flow. A flowchart. Easy to access. Easy to understand. Serious. Professional. It should feel like: We mean Business. That this is very professional. That these principles are world class, world leading process to improve business. It should look very professional, studius, scholarly, an executive would want to see this on her desk and use this tool throughout the day. It cannot be cartoonish in any way. It cannot use clip art or silly things.
Should not have
• Cartoonish. Playful. overly- feminine looking, lacy, frilly, etc.

```html
<!DOCTYPE html>
<html lang="en">
<head>
<meta charset="utf-8">
<title>7-Step Management Process</title>
<link rel="stylesheet" href="https://fonts.googleapis.com/css2?family=Oswald:wght@600;700&display=swap">
<style>
  :root {
    --bg: #ffffff;
    --meetings: #e4dc1c;
    --touchpoint: #0355a3;
    --communication: #9bcb3c;
    --delegation: #ffc214;
    --execution: #3277b5;
    --measurement: #ec1f27;
    --followup: #7fa7d0;
    --core: #f37022;
    --core-dark: #b94a10;
  }
  html, body {
    margin: 0;
    padding: 0;
    overflow: hidden;
    background: var(--bg);
  }
  .process-map {
    display: block;
    width: 825px;
    height: 1200px;
    font-family: "Oswald", "Arial Narrow", sans-serif;
  }
  .step-label {
    font-size: 25px;
    font-weight: 700;
    letter-spacing: 0.6px;
  }
  .connector { fill: none; stroke-width: 1.4; }
  .orbit { fill: none; stroke-width: 1.4; }
  .disc { fill: #ffffff; stroke-width: 11; }

  .meetings      { --c: var(--meetings); }
  .touchpoint    { --c: var(--touchpoint); }
  .communication { --c: var(--communication); }
  .delegation    { --c: var(--delegation); }
  .execution     { --c: var(--execution); }
  .measurement   { --c: var(--measurement); }
  .followup      { --c: var(--followup); }

  .step .disc, .step .orbit { stroke: var(--c); }
  .step .step-label { fill: var(--c); }
  .step .dot { fill: var(--c); }
  .connector { stroke: var(--c); }

  .glyph { fill: var(--c); }
  .glyph .line {
    fill: none;
    stroke: var(--c);
    stroke-width: 4;
    stroke-linecap: round;
    stroke-linejoin: round;
  }
  .glyph .cut { stroke: #ffffff; stroke-width: 2; }
</style>
</head>
<body>
<svg class="process-map" viewBox="0 0 825 1200" xmlns="http://www.w3.org/2000/svg">
  <defs>
    <filter id="lift" x="-30%" y="-30%" width="160%" height="160%">
      <feDropShadow dx="5" dy="7" stdDeviation="5" flood-color="#000" flood-opacity="0.28"/>
    </filter>
    <path id="label-arc" d="M-92,0 A92,92 0 0 1 92,0"/>
    <g id="person">
      <circle cx="0" cy="-7" r="5.5"/>
      <path d="M-10,12 Q-10,0 0,0 Q10,0 10,12 Z"/>
    </g>
  </defs>

  <!-- connectors -->
  <path class="connector meetings" d="M215,254 H295 V530 H330"/>
  <path class="connector touchpoint" d="M215,450 H245 V580 H310"/>
  <path class="connector communication" d="M215,715 H265 V615 H310"/>
  <path class="connector delegation" d="M215,945 H295 V650 H320"/>
  <path class="connector execution" d="M515,560 H550 V365 H615"/>
  <path class="connector measurement" d="M520,594 H615"/>
  <path class="connector followup" d="M515,635 H550 V823 H615"/>

  <!-- left steps -->
  <g class="step meetings" transform="translate(135,254)">
    <path class="orbit" d="M-92,0 A92,92 0 0 0 65,65"/>
    <circle class="dot" cx="-92" cy="0" r="3"/>
    <circle class="disc" r="74" filter="url(#lift)"/>
    <g class="glyph">
      <circle r="12"/>
      <use href="#person" transform="translate(31,0) rotate(90) scale(0.8)"/>
      <use href="#person" transform="translate(15.5,27) rotate(150) scale(0.8)"/>
      <use href="#person" transform="translate(-15.5,27) rotate(210) scale(0.8)"/>
      <use href="#person" transform="translate(-31,0) rotate(270) scale(0.8)"/>
      <use href="#person" transform="translate(-15.5,-27) rotate(330) scale(0.8)"/>
      <use href="#person" transform="translate(15.5,-27) rotate(30) scale(0.8)"/>
    </g>
    <text class="step-label"><textPath href="#label-arc" startOffset="50%" text-anchor="middle">GROUP MEETINGS</textPath></text>
  </g>

  <g class="step touchpoint" transform="translate(135,486)">
    <path class="orbit" d="M-92,0 A92,92 0 0 0 65,65"/>
    <circle class="dot" cx="-92" cy="0" r="3"/>
    <circle class="disc" r="74" filter="url(#lift)"/>
    <g class="glyph">
      <use href="#person" transform="translate(-24,6) scale(1.1)"/>
      <use href="#person" transform="translate(24,6) scale(1.1)"/>
      <path class="line" d="M-10,-2 L6,-8"/>
      <path class="line" d="M-18,-22 Q0,-38 16,-24"/>
      <polygon points="22,-18 10,-20 19,-30"/>
      <path class="line" d="M18,28 Q0,42 -16,30"/>
      <polygon points="-22,24 -10,26 -19,36"/>
    </g>
    <text class="step-label"><textPath href="#label-arc" startOffset="50%" text-anchor="middle">WEEKLYTOUCHPOINT</textPath></text>
  </g>

  <g class="step communication" transform="translate(135,715)">
    <path class="orbit" d="M-92,0 A92,92 0 0 0 65,65"/>
    <circle class="dot" cx="-92" cy="0" r="3"/>
    <circle class="disc" r="74" filter="url(#lift)"/>
    <g class="glyph">
      <use href="#person" transform="translate(-26,10) scale(1.1)"/>
      <use href="#person" transform="translate(26,10) scale(1.1)"/>
      <path class="line" d="M-10,-14 Q2,-24 12,-16"/>
      <polygon points="17,-10 6,-14 15,-22"/>
      <path class="line" d="M10,24 Q-2,34 -12,26"/>
      <polygon points="-17,20 -6,24 -15,32"/>
    </g>
    <text class="step-label"><textPath href="#label-arc" startOffset="50%" text-anchor="middle">CLEAR COMMUNICATION</textPath></text>
  </g>

  <g class="step delegation" transform="translate(135,945)">
    <path class="orbit" d="M-92,0 A92,92 0 0 0 65,65"/>
    <circle class="dot" cx="-92" cy="0" r="3"/>
    <circle class="disc" r="74" filter="url(#lift)"/>
    <g class="glyph">
      <use href="#person" transform="translate(0,-16) scale(1.15)"/>
      <use href="#person" transform="translate(-27,24) scale(0.95)"/>
      <use href="#person" transform="translate(27,24) scale(0.95)"/>
      <path class="line" d="M-14,-12 Q-28,-12 -28,0"/>
      <polygon points="-34,-2 -22,-2 -28,7"/>
      <path class="line" d="M14,-12 Q28,-12 28,0"/>
      <polygon points="34,-2 22,-2 28,7"/>
    </g>
    <text class="step-label"><textPath href="#label-arc" startOffset="50%" text-anchor="middle">DELEGATION</textPath></text>
  </g>

  <!-- core goal -->
  <g class="core-goal" transform="translate(412,594)">
    <circle r="108" fill="#ffffff" stroke="var(--core)" stroke-width="15" filter="url(#lift)"/>
    <circle r="101" fill="none" stroke="var(--core-dark)" stroke-width="2" opacity="0.35"/>
    <circle r="60" fill="var(--core)"/>
    <circle r="46" fill="#ffffff"/>
    <circle r="33" fill="var(--core)"/>
    <circle r="20" fill="#ffffff"/>
    <circle r="9" fill="var(--core)"/>
    <line x1="0" y1="0" x2="52" y2="-52" stroke="var(--core)" stroke-width="6" stroke-linecap="round"/>
    <polygon points="44,-62 70,-70 62,-44 56,-56" fill="var(--core)"/>
  </g>

  <!-- right steps -->
  <g class="step execution" transform="translate(694,358)">
    <path class="orbit" d="M92,0 A92,92 0 0 1 -65,65"/>
    <circle class="dot" cx="92" cy="0" r="3"/>
    <circle class="disc" r="74" filter="url(#lift)"/>
    <g class="glyph">
      <rect x="-40" y="-16" width="20" height="32"/>
      <path class="line cut" d="M-40,-9 H-20 M-40,-3 H-20 M-40,3 H-20 M-40,9 H-20"/>
      <path d="M-18,-12 H12 L38,-10 Q43,-6 38,-2 L14,-2 V4 Q14,9 9,9 V13 Q9,18 3,18 H-18 Z"/>
    </g>
    <text class="step-label"><textPath href="#label-arc" startOffset="50%" text-anchor="middle">EXECUTION</textPath></text>
  </g>

  <g class="step measurement" transform="translate(694,594)">
    <path class="orbit" d="M92,0 A92,92 0 0 1 -65,65"/>
    <circle class="dot" cx="92" cy="0" r="3"/>
    <circle class="disc" r="74" filter="url(#lift)"/>
    <g class="gauge" fill="none" stroke="var(--measurement)" stroke-linecap="round">
      <path d="M-42,18 A45,45 0 1 1 42,18" stroke-width="7"/>
      <path d="M-30,10 L-24,7 M-32,-8 L-25,-7 M-24,-25 L-19,-20 M-9,-34 L-7,-28 M9,-34 L7,-28 M24,-25 L19,-20 M32,-8 L25,-7 M30,10 L24,7" stroke-width="3"/>
      <line x1="0" y1="8" x2="16" y2="-16" stroke-width="4"/>
    </g>
    <circle cx="0" cy="8" r="6" fill="var(--measurement)"/>
    <text class="step-label"><textPath href="#label-arc" startOffset="50%" text-anchor="middle">MEASUREMENT</textPath></text>
  </g>

  <g class="step followup" transform="translate(694,823)">
    <path class="orbit" d="M92,0 A92,92 0 0 1 -65,65"/>
    <circle class="dot" cx="92" cy="0" r="3"/>
    <circle class="disc" r="74" filter="url(#lift)"/>
    <g class="chart-clock" fill="none" stroke="var(--followup)" stroke-width="4" stroke-linecap="round" stroke-linejoin="round">
      <path d="M2,30 H-30 Q-36,30 -36,24 V-28 Q-36,-34 -30,-34 H24 Q30,-34 30,-28 V-2"/>
      <polyline points="-26,6 -12,-10 0,-2 20,-24"/>
      <circle cx="22" cy="22" r="18" fill="#ffffff"/>
      <polyline points="22,11 22,22 30,26"/>
    </g>
    <text class="step-label"><textPath href="#label-arc" startOffset="50%" text-anchor="middle">FOLLOW-UP</textPath></text>
  </g>
</svg>
</body>
</html>
```